eBook Cover

Here is the book title: 27 LESSONS A CHURCH LEADER SHOULD
LEARN ABOUT BUDGETS

Here is the subtitle (or author section): A Tithe Harbor eBook

I've attached the tithe harbor logo below.

Target Market(s)

Church Pastors

Requirements
Must have
• Rocket Logo and Tithe Harbor color palette.
Nice to have
• I have attached some sample book covers that I like

```html
<!DOCTYPE html>
<html lang="en">
<head>
<meta charset="utf-8">
<title>27 Lessons eBook Covers</title>
<link rel="stylesheet" href="https://fonts.googleapis.com/css2?family=Bebas+Neue&family=Montserrat:wght@600&display=swap">
<style>
  :root {
    --page-bg: #ffffff;
    --ink: #55524c;
    --band: #56534c;
    --band-text: #ffffff;
    --yellow: #fcdf00;
    --blue: #009fe0;
    --green: #8cc43f;
  }
  * { margin: 0; padding: 0; box-sizing: border-box; }
  html, body {
    width: 1200px;
    height: 700px;
    overflow: hidden;
    background: var(--page-bg);
  }
  .canvas {
    position: relative;
    width: 1200px;
    height: 700px;
  }
  .cover {
    position: absolute;
    top: 69px;
    width: 365px;
    height: 583px;
  }
  .cover--yellow { left: 12px;  background: var(--yellow); }
  .cover--blue   { left: 408px; background: var(--blue); }
  .cover--green  { left: 804px; background: var(--green); }

  .cover__title {
    position: absolute;
    top: 66px;
    left: 0;
    width: 100%;
    font-family: "Bebas Neue", "Arial Narrow", sans-serif;
    font-weight: 400;
    font-size: 60px;
    line-height: 64.5px;
    letter-spacing: 1px;
    color: var(--ink);
    text-align: center;
  }
  .cover__title span { display: block; }

  .cover__footer {
    position: absolute;
    left: 0;
    bottom: 0;
    width: 100%;
    height: 76px;
    display: flex;
  }
  .cover__series {
    width: 252px;
    height: 100%;
    background: var(--band);
    color: var(--band-text);
    font-family: "Montserrat", Arial, sans-serif;
    font-weight: 600;
    font-size: 12.5px;
    letter-spacing: 1.6px;
    display: flex;
    align-items: center;
    padding-left: 10px;
    white-space: nowrap;
  }
  .cover__series .lower { text-transform: none; }

  .brand {
    flex: 1;
    height: 100%;
    display: flex;
    align-items: center;
    justify-content: center;
    font-family: "Montserrat", Arial, sans-serif;
    font-weight: 600;
    font-size: 12.5px;
    letter-spacing: 1.6px;
    color: var(--ink);
    white-space: nowrap;
  }
  .brand--green  { background: var(--green); }
  .brand--yellow { background: var(--yellow); }
</style>
</head>
<body>
<main class="canvas">

  <article class="cover cover--yellow">
    <h1 class="cover__title">
      <span>27 LESSONS</span><span>A CHURCH</span><span>LEADER</span><span>SHOULD</span><span>LEARN ABOUT</span><span>BUDGETS</span>
    </h1>
    <footer class="cover__footer">
      <p class="cover__series">A TITHE HARBOR&nbsp;<span class="lower">eBOOK</span></p>
      <p class="brand brand--green">HARBOR CO.</p>
    </footer>
  </article>

  <article class="cover cover--blue">
    <h1 class="cover__title">
      <span>27 LESSONS</span><span>A CHURCH</span><span>LEADER</span><span>SHOULD</span><span>LEARN ABOUT</span><span>BUDGETS</span>
    </h1>
    <footer class="cover__footer">
      <p class="cover__series">A TITHE HARBOR&nbsp;<span class="lower">eBOOK</span></p>
      <p class="brand brand--green">HARBOR CO.</p>
    </footer>
  </article>

  <article class="cover cover--green">
    <h1 class="cover__title">
      <span>27 LESSONS</span><span>A CHURCH</span><span>LEADER</span><span>SHOULD</span><span>LEARN ABOUT</span><span>BUDGETS</span>
    </h1>
    <footer class="cover__footer">
      <p class="cover__series">A TITHE HARBOR&nbsp;<span class="lower">eBOOK</span></p>
      <p class="brand brand--yellow">HARBOR CO.</p>
    </footer>
  </article>

</main>
</body>
</html>
```